Need Web Design for Business Process Outsourcing Company (Kelmora)

Kelmora is a business process outsourcing company. Need a simple site similar to http://www.tarvenholm.com/ but with a more professional and credible look. New to the process; not sure where to start and comparing my options. Please let me know what my options are if I choose to go with you. Logo is attached for your reference. Please use same colorway

Reason: I want the final product to be coded. Please confirm you will be able to code final design.

Industry/Entity Type

Business

Coding

Coded - Design and coding required

```html
<!DOCTYPE html>
<html lang="en">
<head>
<meta charset="utf-8">
<title>Kelmora Services</title>
<link href="https://fonts.googleapis.com/css2?family=Raleway:wght@600;700;800&family=Open+Sans:wght@400;600;700&family=Montserrat:wght@600;700&display=swap" rel="stylesheet">
<style>
:root{
  --brand:#1a8fd0;
  --brand-deep:#0b5a94;
  --footer:#0d4f87;
  --footer-deep:#083e6c;
  --ink:#1f1f1f;
  --muted:#777;
  --line:#dcdcdc;
  --soft:#f5f5f5;
  --star:#f0962e;
  --white:#fff;
}
*{margin:0;padding:0;box-sizing:border-box}
html,body{width:1200px;height:2609px;overflow:hidden;background:var(--white)}
body{position:relative;font-family:'Open Sans',sans-serif;color:var(--ink)}
.abs{position:absolute}

/* header */
.site-header{left:0;top:0;width:1200px;height:104px;background:var(--white)}
.logo{left:99px;top:26px;display:flex;align-items:center;gap:12px}
.logo-mark{width:52px;height:52px;background:var(--brand)}
.logo-name{font-family:'Open Sans',sans-serif;font-weight:700;font-size:42px;color:var(--brand-deep);letter-spacing:-.5px;line-height:52px}
.contact-chip{display:flex;align-items:center;gap:14px}
.chip-icon{width:48px;height:48px;border-radius:50%;background:var(--brand);display:flex;align-items:center;justify-content:center}
.chip-label{font-size:13px;color:#555;line-height:1.3}
.chip-value{font-size:18px;font-weight:700;color:var(--ink);line-height:1.3}

.nav{left:0;top:104px;width:1200px;height:49px;background:var(--brand-deep)}
.nav ul{list-style:none;display:flex;position:absolute;left:97px;top:0;height:49px}
.nav li{font-size:12px;color:var(--white);text-transform:uppercase;line-height:49px;padding:0 17px;font-weight:600}
.nav li.active{background:var(--brand);padding:0 27px}

/* hero */
.hero{left:0;top:153px;width:1200px;height:534px}
.hero-title{left:643px;top:448px;font-family:'Raleway',sans-serif;font-weight:800;font-size:46px;color:var(--white);letter-spacing:.5px;white-space:nowrap}
.hero-sub{left:643px;top:508px;font-size:17px;color:var(--white);white-space:nowrap}

/* section titles */
.section-title{width:1200px;left:0;text-align:center;font-family:'Raleway',sans-serif;font-weight:700;font-size:30px;text-transform:uppercase}
.divider{left:492px;width:216px;height:4px}

/* service cards */
.card{top:840px;width:232px;height:221px;border:1px solid var(--line);text-align:center}
.card svg{position:absolute;left:86px;top:30px}
.card-rule{position:absolute;left:86px;top:107px;width:60px;border-top:1px dashed #9ab}
.card h3{position:absolute;top:124px;width:100%;font-size:15px;font-weight:600;color:var(--brand);text-transform:uppercase}
.card p{position:absolute;top:150px;left:10px;right:10px;font-size:12px;line-height:25px;color:#666}

/* what we do */
.whatwedo{left:0;top:1122px;width:1200px;height:448px;background:linear-gradient(180deg,#1b93d4,#1786c6)}
.feature-icon{flex:none;width:106px;height:106px;border-radius:50%;border:3px solid var(--white);background:var(--brand-deep);display:flex;align-items:center;justify-content:center}
.feature h4{font-size:16px;font-weight:700;color:var(--white);text-transform:uppercase}
.feature p{margin-top:14px;font-size:12px;line-height:23px;color:#e8f3fb;width:340px}

/* about */
.about-img{left:99px;top:1631px;width:492px;height:275px}
.about-title{left:642px;top:1624px;font-family:'Montserrat',sans-serif;font-weight:700;font-size:27px;line-height:40px;text-transform:uppercase;color:var(--ink)}
.about-text{left:642px;top:1722px;width:468px;font-size:13px;line-height:22.6px;color:#777}
.btn{left:642px;top:1871px;width:114px;height:37px;background:var(--brand);color:var(--white);font-size:13px;text-transform:uppercase;display:flex;align-items:center;justify-content:center}

/* testimonials */
.testimonials{left:0;top:1974px;width:1200px;height:321px;background:var(--soft)}
.testi-sub{left:0;width:1200px;text-align:center;top:2067px;font-family:Georgia,serif;font-style:italic;font-size:14px;color:#999}
.avatar{width:129px;height:112px;border:3px solid var(--white);box-shadow:0 0 0 1px #ddd}
.testi-name{font-size:16px;font-weight:600;text-transform:uppercase;color:var(--ink)}
.testi-role{font-size:12px;color:#aaa;margin-top:4px}
.testi-role span{color:var(--star);letter-spacing:1px;margin-left:14px}
.testi-text{font-size:13px;line-height:23px;color:#777;width:330px}
.quote{font-family:Georgia,serif;font-size:80px;color:#ddd;line-height:1}

/* footer */
.footer{left:0;top:2295px;width:1200px;height:258px;background:var(--footer)}
.footer-col{position:absolute;top:2338px}
.footer-col h5{font-family:'Raleway',sans-serif;font-size:17px;font-weight:700;color:var(--white);text-transform:uppercase}
.footer-col p,.footer-col li{font-size:12px;color:#dde9f4;line-height:22px}
.footer-col ul{list-style:none;margin-top:18px}
.footer-col ul li{line-height:30px}
.contact-line{display:flex;gap:12px;align-items:flex-start;margin-top:10px}
.contact-line svg{flex:none;margin-top:4px}
.read-more{font-size:10px;color:#3aa6e3;text-transform:uppercase;margin-top:20px}
.copyright{left:0;top:2553px;width:1200px;height:56px;background:var(--footer-deep);color:#dde9f4;font-size:12px;text-align:center;line-height:56px}
</style>
</head>
<body>

<header class="abs site-header">
  <div class="abs logo">
    <div class="logo-mark"></div>
    <div class="logo-name">Kelmora</div>
  </div>
  <div class="abs contact-chip" style="left:573px;top:26px">
    <div class="chip-icon">
      <svg width="22" height="22" viewBox="0 0 24 24"><path fill="#fff" d="M6.6 10.8c1.4 2.8 3.8 5.1 6.6 6.6l2.2-2.2c.3-.3.7-.4 1-.2 1.1.4 2.3.6 3.6.6.6 0 1 .4 1 1V20c0 .6-.4 1-1 1C10.6 21 3 13.4 3 4c0-.6.4-1 1-1h3.5c.6 0 1 .4 1 1 0 1.3.2 2.5.6 3.6.1.3 0 .7-.2 1z"/></svg>
    </div>
    <div><div class="chip-label">Call us on</div><div class="chip-value">+ 1 541 608 2290</div></div>
  </div>
  <div class="abs contact-chip" style="left:821px;top:26px">
    <div class="chip-icon">
      <svg width="22" height="22" viewBox="0 0 24 24"><path fill="#fff" d="M3 5h18v14H3z"/><path fill="none" stroke="#1a8fd0" stroke-width="2" d="M3 6l9 7 9-7"/></svg>
    </div>
    <div><div class="chip-label">Mail us on</div><div class="chip-value">info@kelmoramail.com</div></div>
  </div>
</header>

<nav class="abs nav">
  <ul>
    <li class="active">Home</li><li>About Us</li><li>Who We Are</li><li>Our Solutions</li><li>Our Strategy</li><li>Our Experience</li><li>Security</li><li>News</li><li>Contact Us</li>
  </ul>
</nav>

<section>
  <svg class="abs hero" viewBox="0 0 1200 534" role="img" aria-label="Hero photo: person looking through a telescope over a city skyline at sunset">
    <defs>
      <linearGradient id="sky" x1="0" y1="0" x2="0" y2="1">
        <stop offset="0" stop-color="#e9c4a6"/>
        <stop offset=".45" stop-color="#c9808c"/>
        <stop offset="1" stop-color="#5a3f86"/>
      </linearGradient>
      <radialGradient id="sun" cx=".3" cy=".45" r=".35">
        <stop offset="0" stop-color="#f7c07a" stop-opacity=".8"/>
        <stop offset="1" stop-color="#f7c07a" stop-opacity="0"/>
      </radialGradient>
      <linearGradient id="shade" x1="0" y1="0" x2="1" y2="0">
        <stop offset="0" stop-color="#3b2c5e" stop-opacity=".6"/>
        <stop offset=".45" stop-color="#3b2c5e" stop-opacity="0"/>
      </linearGradient>
    </defs>
    <path d="M0 0H1200V466Q600 620 0 466Z" fill="url(#sky)"/>
    <path d="M0 0H1200V466Q600 620 0 466Z" fill="url(#sun)"/>
    <path d="M0 0H1200V466Q600 620 0 466Z" fill="url(#shade)"/>
    <path d="M50 175L36 212 50 249" fill="none" stroke="#fff" stroke-width="2" opacity=".85"/>
    <path d="M1150 175L1164 212 1150 249" fill="none" stroke="#fff" stroke-width="2" opacity=".85"/>
  </svg>
  <h1 class="abs hero-title">KELMORA SERVICES</h1>
  <p class="abs hero-sub">We are a BPO business process outsourcing company.</p>
</section>

<section>
  <h2 class="abs section-title" style="top:740px">Kelmora Outsourcing Services</h2>
  <svg class="abs divider" style="top:795px" viewBox="0 0 216 4"><line x1="0" y1="2" x2="216" y2="2" stroke="#1a8fd0" stroke-dasharray="3 3" stroke-width="1"/><rect x="78" y="0" width="60" height="4" fill="#0b5a94"/></svg>

  <div class="abs card" style="left:97px">
    <svg width="60" height="66" viewBox="0 0 60 66"><circle cx="30" cy="20" r="14" fill="#555"/><path d="M14 22a16 16 0 0 1 32 0" fill="none" stroke="#555" stroke-width="3"/><rect x="10" y="18" width="6" height="12" rx="2" fill="#555"/><rect x="44" y="18" width="6" height="12" rx="2" fill="#555"/><path d="M4 66c0-16 12-26 26-26s26 10 26 26z" fill="#555"/></svg>
    <div class="card-rule"></div>
    <h3>Customer Service</h3>
    <p>Contrary to popular belief, Lorem Ipsum is not simply random text.</p>
  </div>
  <div class="abs card" style="left:355px">
    <svg width="60" height="66" viewBox="0 0 60 66"><circle cx="28" cy="16" r="13" fill="#1a8fd0"/><path d="M6 60c0-18 10-28 22-28s22 10 22 28z" fill="#1a8fd0"/><circle cx="40" cy="52" r="11" fill="#0b5a94" stroke="#fff" stroke-width="2"/><path d="M40 46v12M34 52h12" stroke="#fff" stroke-width="2.5"/></svg>
    <div class="card-rule"></div>
    <h3>Request Assistance</h3>
    <p>Contrary to popular belief, Lorem Ipsum is not simply random text.</p>
  </div>
  <div class="abs card" style="left:613px">
    <svg width="70" height="66" viewBox="0 0 70 66" style="left:81px"><path d="M18 48H14a12 12 0 0 1 0-24 18 18 0 0 1 34-6 14 14 0 0 1 8 30h-4" fill="none" stroke="#555" stroke-width="3"/><path d="M35 60V30M27 38l8-8 8 8" fill="none" stroke="#555" stroke-width="3"/></svg>
    <div class="card-rule"></div>
    <h3>IT Solutions</h3>
    <p>Contrary to popular belief, Lorem Ipsum is not simply random text.</p>
  </div>
  <div class="abs card" style="left:871px">
    <svg width="66" height="66" viewBox="0 0 66 66"><circle cx="14" cy="14" r="7" fill="#555"/><circle cx="50" cy="14" r="7" fill="#555"/><path d="M2 40c0-10 5-16 12-16s10 4 10 8H2z" fill="#555"/><path d="M40 32c0-4 3-8 10-8s12 6 12 16H40z" fill="#555"/><circle cx="32" cy="32" r="13" fill="#fff" stroke="#555" stroke-width="4"/><circle cx="32" cy="29" r="4" fill="#555"/><path d="M25 39c1-4 4-5 7-5s6 1 7 5" fill="#555"/><path d="M42 42l14 14" stroke="#555" stroke-width="6" stroke-linecap="round"/></svg>
    <div class="card-rule"></div>
    <h3>Human Resources</h3>
    <p>Contrary to popular belief, Lorem Ipsum is not simply random text.</p>
  </div>
</section>

<section class="abs whatwedo">
  <h2 class="abs section-title" style="top:41px;color:#fff;font-size:28px">What We Do</h2>
  <svg class="abs divider" style="top:94px" viewBox="0 0 216 4"><line x1="4" y1="2" x2="212" y2="2" stroke="#fff" stroke-dasharray="3 3" stroke-width="1"/><rect x="63" y="0" width="90" height="4" fill="#fff"/></svg>

  <div class="abs feature" style="left:98px;top:133px;display:flex;gap:28px">
    <div class="feature-icon"><svg width="46" height="40" viewBox="0 0 46 40"><rect x="3" y="10" width="40" height="28" rx="4" fill="#fff"/><path d="M16 10V5h14v5" fill="none" stroke="#fff" stroke-width="3"/><rect x="19" y="20" width="8" height="6" fill="#0b5a94"/></svg></div>
    <div style="padding-top:8px"><h4>Reinventing Services</h4><p>There are many variations of passages of Lorem Ipsum available, but the majority have suffered alteration in some form, by injected humour, or randomised words</p></div>
  </div>
  <div class="abs feature" style="left:637px;top:133px;display:flex;gap:28px">
    <div class="feature-icon"><svg width="44" height="48" viewBox="0 0 44 48"><path d="M20 3L4 9v14c0 12 7 20 16 23 9-3 16-11 16-23V9z" fill="none" stroke="#fff" stroke-width="3"/><circle cx="31" cy="30" r="10" fill="#fff"/><path d="M26 30l4 4 6-7" fill="none" stroke="#0b5a94" stroke-width="2.5"/></svg></div>
    <div style="padding-top:8px"><h4>Security</h4><p>There are many variations of passages of Lorem Ipsum available, but the majority have suffered alteration in some form, by injected humour, or randomised words</p></div>
  </div>
  <div class="abs feature" style="left:98px;top:289px;display:flex;gap:28px">
    <div class="feature-icon"><svg width="46" height="46" viewBox="0 0 46 46"><path d="M4 12L23 4l19 8-19 8z" fill="#fff"/><rect x="8" y="20" width="30" height="18" fill="#fff"/><path d="M14 24v10M20 24v10M26 24v10M32 24v10" stroke="#0b5a94" stroke-width="2"/><path d="M4 42h38" stroke="#fff" stroke-width="3"/></svg></div>
    <div style="padding-top:8px"><h4>Our Facilities</h4><p>There are many variations of passages of Lorem Ipsum available, but the majority have suffered alteration in some form, by injected humour, or randomised words</p></div>
  </div>
  <div class="abs feature" style="left:637px;top:289px;display:flex;gap:28px">
    <div class="feature-icon"><svg width="50" height="44" viewBox="0 0 50 44"><rect x="20" y="6" width="26" height="6" fill="#fff"/><rect x="20" y="15" width="26" height="6" fill="#fff"/><rect x="20" y="24" width="26" height="6" fill="#fff"/><rect x="20" y="33" width="26" height="6" fill="#fff"/><circle cx="16" cy="26" r="13" fill="#fff" stroke="#0b5a94" stroke-width="2"/><text x="16" y="32" text-anchor="middle" font-family="Open Sans,sans-serif" font-weight="700" font-size="17" fill="#0b5a94">$</text></svg></div>
    <div style="padding-top:8px"><h4>Financial Status</h4><p>There are many variations of passages of Lorem Ipsum available, but the majority have suffered alteration in some form, by injected humour, or randomised words</p></div>
  </div>
</section>

<section>
  <svg class="abs about-img" viewBox="0 0 492 275" role="img" aria-label="Photo: businessman touching a glowing cloud network of people icons">
    <defs><radialGradient id="glow" cx=".55" cy=".4" r=".7"><stop offset="0" stop-color="#2a6fb3"/><stop offset=".6" stop-color="#0d2c56"/><stop offset="1" stop-color="#050d1f"/></radialGradient></defs>
    <rect width="492" height="275" fill="url(#glow)"/>
  </svg>
  <h2 class="abs about-title">We Are A BPO Business Process<br>Outsourcing Company</h2>
  <p class="abs about-text">At vero eos et accusamus et iusto odio dignissimos ducimus qui blanditiis praesentium voluptatum deleniti atque corrupti quos dolores et quas molestias excepturi sint occaecati cupiditate non provident, similique sunt in culpa qui officia deserunt mollitia animi, id est laborum et dolorum fuga. Et harum quidem rerum facilis est et expedita distinctio.</p>
  <div class="abs btn">Read More</div>
</section>

<section class="abs testimonials"></section>
<h2 class="abs section-title" style="top:2025px;font-family:'Montserrat',sans-serif;font-size:28px;color:#222">Our Client Testimonial</h2>
<p class="abs testi-sub">What Our Client Says About us</p>

<div class="abs avatar" style="left:97px;top:2116px;background:linear-gradient(135deg,#8a6a4e,#c9a383 60%,#5b4a3c)" role="img" aria-label="Client portrait photo"></div>
<div class="abs" style="left:245px;top:2114px"><div class="testi-name">Marcus T.</div><div class="testi-role">Customers <span>★★★★★</span></div></div>
<div class="abs quote" style="left:474px;top:2104px">&#8221;</div>
<p class="abs testi-text" style="left:245px;top:2168px">At vero eos et accusamus et iusto odio dignissimos ducimus qui blanditiis praesentium voluptatum deleniti atque corrupti quos dolores</p>

<div class="abs avatar" style="left:636px;top:2116px;background:linear-gradient(135deg,#7d6a58,#e0c7a7 60%,#a58d72)" role="img" aria-label="Client portrait photo"></div>
<div class="abs" style="left:784px;top:2114px"><div class="testi-name">Elena R.</div><div class="testi-role">Customers <span>★★★★★</span></div></div>
<div class="abs quote" style="left:1012px;top:2104px">&#8221;</div>
<p class="abs testi-text" style="left:784px;top:2168px">At vero eos et accusamus et iusto odio dignissimos ducimus qui blanditiis praesentium voluptatum deleniti atque corrupti quos dolores</p>

<footer>
  <div class="abs footer"></div>
  <div class="footer-col" style="left:97px;width:230px">
    <h5>About Us</h5>
    <p style="margin-top:20px">There are many variations of passages of Lorem Ipsum available, but the majority have suffered alteration</p>
    <div class="read-more">Read More</div>
  </div>
  <div class="footer-col" style="left:376px;width:230px">
    <h5>Contact Us</h5>
    <div class="contact-line" style="margin-top:16px"><svg width="12" height="14" viewBox="0 0 12 16"><path d="M6 0a6 6 0 0 1 6 6c0 4-6 10-6 10S0 10 0 6a6 6 0 0 1 6-6z" fill="#fff"/><circle cx="6" cy="6" r="2" fill="#0d4f87"/></svg><p>1820 Harbor Row Suite 4<br>Port Alden Oregon 97410</p></div>
    <div class="contact-line"><svg width="12" height="14" viewBox="0 0 24 24"><path fill="#fff" d="M6.6 10.8c1.4 2.8 3.8 5.1 6.6 6.6l2.2-2.2c.3-.3.7-.4 1-.2 1.1.4 2.3.6 3.6.6.6 0 1 .4 1 1V20c0 .6-.4 1-1 1C10.6 21 3 13.4 3 4c0-.6.4-1 1-1h3.5c.6 0 1 .4 1 1 0 1.3.2 2.5.6 3.6.1.3 0 .7-.2 1z"/></svg><p>Phone -541-608-2290</p></div>
    <div class="contact-line"><svg width="13" height="14" viewBox="0 0 14 14"><rect x="3" y="0" width="8" height="4" fill="#fff"/><rect x="0" y="4" width="14" height="7" fill="#fff"/><rect x="3" y="9" width="8" height="5" fill="#fff" stroke="#0d4f87"/></svg><p>Fax - (541) 608-2291</p></div>
    <div class="contact-line"><svg width="13" height="14" viewBox="0 0 14 12"><rect x=".5" y=".5" width="13" height="11" fill="none" stroke="#fff"/><path d="M1 1l6 5 6-5" fill="none" stroke="#fff"/></svg><p>E-mail - info@example.com</p></div>
  </div>
  <div class="footer-col" style="left:621px">
    <h5>Quick Links</h5>
    <ul><li>About us</li><li>Support</li><li>Who we are</li></ul>
  </div>
  <div class="footer-col" style="left:805px">
    <h5>Our Policy</h5>
    <ul><li>Help &amp; Contact</li><li>Out sourcing</li><li>Affiliates</li></ul>
  </div>
  <div class="footer-col" style="left:996px">
    <h5>Community</h5>
    <ul><li>Guidelines</li><li>Terms &amp; conditions</li><li>privacy policy</li><li>Contact us</li></ul>
  </div>
  <div class="abs copyright">Copyright ©2016 Company Name. All rights reserved.</div>
</footer>

</body>
</html>
```